AI Layout work for Business Cards, Letterhead and Compliment Slip for Award-winning UK Property Deve

No actual logo or corporate identity design work needed here but some skill required to create layouts for business card, letterhead and compliment slip for this award-winning company.
I can provide AI files featuring the company logo and an initial layout of the business card, (6 versions featuring the same design but for different personnel), along with some initial instructions (with possibly more to follow from the client). The finished layouts for each item need to be print-ready in AI format - 8 in all (6 for each business card plus 1 for letterhead and 1 for compliment slip).
I've given this project a 5-day duration but there may be some flexibility built into that depending on client feedback. Hopefully that won't be a problem.
UPDATE:
The client has been very prescriptive about the layout and design of these. To that end, please find 3 additional pdfs that explain what's required.
1.
All BUSINESS CARDS need to be laid out as per the attached AI file (but see latest pdf to check which layout - there are 2 in the original AI file). Use the details in the VEL-contact-details.pdf to create 6 individual AI files, one for each card.
2.
Create 2 additional AI files, one each for the LETTERHEAD and the COMPLIMENT SLIP based on the latest mock-up that I've provided (letterhead-layout-final.pdf)
In all, I need EIGHT individual AI files, 6 for each business card, 1 for the letterhead and 1 for the compliment slip. I'd like to get this done as soon as possible now please.
Target Market(s)
Purchasers of upmarket luxury properties - see here: http://www.velproperties.co.uk
Industry/Entity Type
Business
Requirements
Must have
- Layouts need to be cool, understated and uncluttered.
Nice to have
- Please keep it simple! The actual logo background colour is likely to change (awaiting confirmation from client) but accompanying text detail and font (Deja Vu Sans Condensed) can remain as seen in the files below - for the time being at least! That having been said, I'm open to suggestions.
Should not have
- Nothing extreme or ostentatious please.

```html
<!DOCTYPE html>
<html lang="en">
<head>
<meta charset="utf-8">
<title>VEL Exclusive Properties – Business Card</title>
<link href="https://fonts.googleapis.com/css2?family=Noto+Sans:wdth,wght@87.5,400;87.5,700&display=swap" rel="stylesheet">
<style>
  :root {
    --backdrop: #d9d9d9;
    --card: #f4f4f2;
    --navy: #17275c;
    --ink: #111111;
    --ink-soft: #3a3a3a;
    --rule: #6d6d6d;
  }
  * { box-sizing: border-box; margin: 0; padding: 0; }
  html, body {
    width: 1200px; height: 1200px; overflow: hidden;
    background: var(--backdrop);
    font-family: "Noto Sans", "DejaVu Sans Condensed", sans-serif;
    font-stretch: 87.5%;
  }
  .canvas {
    position: relative; width: 1200px; height: 1200px;
    display: flex; flex-direction: column; align-items: center; justify-content: center; gap: 60px;
  }
  .card {
    position: relative; width: 630px; height: 360px;
    background: var(--card);
    box-shadow: 0 2px 6px rgba(0,0,0,.12);
  }
  .brand { display: flex; align-items: center; gap: 14px; color: var(--navy); }
  .brand__mark { width: 34px; height: 34px; background: var(--navy); }
  .brand__name { font-size: 64px; font-weight: 700; letter-spacing: 2px; line-height: 1; }

  /* contact side */
  .card--contact .brand { position: absolute; left: 44px; top: 56px; }
  .address {
    position: absolute; left: 44px; top: 150px;
    font-size: 15px; line-height: 1.4; color: var(--ink-soft);
  }
  .divider { position: absolute; left: 330px; top: 56px; width: 1px; height: 150px; background: var(--rule); }
  .person { position: absolute; right: 44px; top: 112px; text-align: right; }
  .person__name { font-size: 30px; font-weight: 700; color: var(--ink); line-height: 1.1; }
  .person__role { font-size: 22px; color: var(--ink); }
  .contact {
    position: absolute; right: 44px; top: 218px; text-align: right;
    font-size: 17px; line-height: 1.45; color: var(--ink);
  }

  /* logo side */
  .card--logo { display: flex; flex-direction: column; align-items: center; justify-content: center; gap: 18px; }
  .card--logo .brand__name { font-size: 84px; }
  .card--logo .brand__mark { width: 44px; height: 44px; }
  .web { font-size: 22px; color: var(--ink); }
</style>
</head>
<body>
<main class="canvas">
  <section class="card card--contact" aria-label="Business card, contact side">
    <div class="brand">
      <span class="brand__mark"></span>
      <span class="brand__name">VEL</span>
    </div>
    <p class="address">VEL Exclusive Properties<br>Oak Barn House,<br>Oak Barn Lane<br>Little Marden HX9 2QT</p>
    <span class="divider"></span>
    <div class="person">
      <p class="person__name">Daniel Hart</p>
      <p class="person__role">Director</p>
    </div>
    <p class="contact">+44 (0)1632 960482<br>enquiries@velproperties.co.uk<br>velproperties.co.uk</p>
  </section>

  <section class="card card--logo" aria-label="Business card, logo side">
    <div class="brand">
      <span class="brand__mark"></span>
      <span class="brand__name">VEL</span>
    </div>
    <p class="web">www.velproperties.co.uk</p>
  </section>
</main>
</body>
</html>
```